依頼詳細
チラシ配布のため、デザイン製作をお願いします。
パッとみて印象に残り、何が強みなのか解りやすくアピールできればと思います。
記載項目
こちらに使用して頂きたいテキストを添付ファイルにまとめました。

イラストなどを使用して印象に残るデザインを作成して頂けると助かります。
必要に応じてテキストを追加して頂いても問題ありませんので
宜しくお願い致します。

サイトURLが記載されてますが、リニューアル予定ですので
サイトのデザインは参考にしないようお願い致します。
サイズ
A4
ページ数
片面
希望イメージ
シンプル 複雑
単色 カラフル
暗い 明るい
日常 高級
遊び心 厳粛
未来的 伝統的
女性的 男性的
希望する色
水色系、緑系、黄・オレンジ系
納品ファイル
• 高解像度JPG (.jpg)
• イラストレーター形式 (.ai)
• フォトショップ形式 (.psd)
補足説明
■ 選んだ理由

希望のデザインでした。

■ 提案者全員のお礼・コメント

参加いただき感謝です。
ありがとうございます。

```html
<!DOCTYPE html>
<html lang="ja">
<head>
<meta charset="utf-8">
<title>遺品整理・お片づけ チラシ</title>
<link href="https://fonts.googleapis.com/css2?family=M+PLUS+Rounded+1c:wght@500;800&family=Noto+Sans+JP:wght@400;700;900&display=swap" rel="stylesheet">
<style>
:root{
  --sky:#dcebf7;
  --blue:#1f6fb8;
  --blue-deep:#16508c;
  --blue-mid:#3a8bd0;
  --green:#2fa83a;
  --orange:#f08a00;
  --ink:#222;
  --white:#fff;
  --yellow:#fff35a;
}
*{margin:0;padding:0;box-sizing:border-box}
html,body{width:846px;height:1200px;overflow:hidden;background:var(--white)}
body{font-family:"Noto Sans JP",sans-serif;color:var(--ink)}
.flyer{position:relative;width:846px;height:1200px;overflow:hidden;background:var(--white)}
.hero-bg{position:absolute;left:0;top:0;width:846px;height:440px;background:var(--sky)}
.house{position:absolute;left:0;top:0}
.title{position:absolute;left:34px;top:186px;font-family:"M PLUS Rounded 1c","Noto Sans JP",sans-serif;font-weight:800;font-size:96px;line-height:108px;color:var(--white);letter-spacing:4px;white-space:nowrap}
.worker-top{position:absolute;left:610px;top:0;width:236px;height:290px;background:linear-gradient(#bfd9ee,#9cc3e4);border-radius:0 0 0 40px}
.free-badge{position:absolute;left:672px;top:140px;width:156px;height:156px;border-radius:50%;background:var(--green);border:5px solid var(--white);color:var(--white);text-align:center;font-weight:900}
.free-badge .small{display:block;margin-top:26px;font-size:21px;line-height:26px}
.free-badge .big{display:block;font-size:42px;line-height:52px;color:var(--yellow)}
.catch{position:absolute;left:0;top:428px;width:846px;height:64px;background:var(--white);text-align:center;font-size:44px;font-weight:900;line-height:64px;letter-spacing:2px;white-space:nowrap}
.catch-line{position:absolute;left:30px;top:494px;width:786px;height:4px;background:var(--blue)}
.couple{position:absolute;left:28px;top:512px;width:240px;height:232px;background:linear-gradient(#f3e6d6,#e3d0b8);border-radius:12px}
.worries{position:absolute;left:285px;top:515px;width:535px}
.worries .lead{color:var(--blue);font-size:26px;font-weight:900;line-height:38px;white-space:nowrap}
.worries .sub{color:var(--blue-deep);font-size:20px;font-weight:700;line-height:32px;border-bottom:2px dotted var(--blue);padding-bottom:6px;white-space:nowrap}
.worries .body{font-size:15px;line-height:25px;margin-top:10px}
.services{position:absolute;left:28px;top:760px;width:272px;display:grid;grid-template-columns:1fr 1fr;gap:6px}
.services li{list-style:none;height:40px;line-height:40px;text-align:center;color:var(--white);font-weight:700;font-size:19px;border-radius:4px;white-space:nowrap}
.services .g{background:var(--green)}
.services .o{background:var(--orange)}
.services .all{background:none;color:var(--ink);font-weight:900;font-size:19px}
.items{position:absolute;left:308px;top:752px;width:286px;height:210px;background:linear-gradient(#efe6d8,#d9c6a8);border-radius:10px}
.worker-bottom{position:absolute;left:600px;top:740px;width:226px;height:226px;background:linear-gradient(#cfe2f2,#9cc3e4);border-radius:10px}
.heart{position:absolute;left:28px;top:1000px;font-size:20px;font-weight:700;color:var(--blue-deep)}
.company{position:absolute;left:28px;top:1032px;width:272px;height:72px;border:2px solid var(--blue);text-align:center;font-size:19px;font-weight:700;line-height:32px;padding-top:3px}
.license{position:absolute;left:28px;top:1112px;width:320px;font-size:11px;line-height:17px}
.call-bar{position:absolute;left:380px;top:972px;width:440px;height:38px;background:var(--blue);color:var(--white);text-align:center;font-size:21px;font-weight:900;line-height:38px;border-radius:19px;white-space:nowrap}
.tel{position:absolute;left:380px;top:1016px;width:446px;height:56px;display:flex;align-items:center;gap:6px;color:var(--orange);font-weight:900;white-space:nowrap}
.tel svg{flex:none}
.tel .label{font-size:44px;line-height:56px}
.tel .num{font-size:46px;line-height:56px;letter-spacing:-1px}
.info{position:absolute;left:380px;top:1078px;width:446px;font-size:14px;line-height:22px;white-space:nowrap}
.info b{color:var(--blue-deep)}
.footer{position:absolute;left:0;top:1170px;width:846px;height:30px;background:var(--sky)}
</style>
</head>
<body>
<main class="flyer">
  <div class="hero-bg"></div>
  <svg class="house" width="846" height="440" viewBox="0 0 846 440">
    <polygon points="0,176 310,22 620,176 620,420 0,420" fill="var(--blue-mid)" stroke="var(--blue-deep)" stroke-width="10" stroke-linejoin="round"/>
  </svg>
  <h1 class="title">遺品整理<br>お片づけ</h1>
  <div class="worker-top" role="img" aria-label="指をさす作業服姿のスタッフのイラスト"></div>
  <div class="free-badge"><span class="small">ご相談・<br>お見積り</span><span class="big">無料</span></div>

  <p class="catch">私たちプロにおまかせください!</p>
  <div class="catch-line"></div>

  <div class="couple" role="img" aria-label="困っている高齢の夫婦のイラスト"></div>
  <div class="worries">
    <p class="lead">何から手をつけたら良いか分からない…</p>
    <p class="sub">自分じゃ片付け方が分からずお困りじゃありませんか？</p>
    <p class="body">株式会社リニューでは故人様の大切な遺品を整理するお手伝いをいたします。ご遺族様の確認のもと、不用品の処分または買取をさせていただき、段ボール箱からご家族までどんな状況でもお客様をご負担の少ない形で整理・清掃いたします。お気軽にご相談ください。</p>
  </div>

  <ul class="services">
    <li class="g">不用品回収</li><li class="o">仕分け</li>
    <li class="g">貴重品探索</li><li class="o">特殊清掃</li>
    <li class="g">片付け</li><li class="o">清掃</li>
    <li class="g">貴重品買取</li><li class="o">生前整理</li>
    <li class="g">リフォーム</li><li class="all">各種承ります!</li>
  </ul>

  <div class="items" role="img" aria-label="箪笥や段ボール、衣類など遺品のイラスト"></div>
  <div class="worker-bottom" role="img" aria-label="段ボールを運ぶスタッフのイラスト"></div>

  <p class="heart">心をこめて遺品整理</p>
  <div class="company">株式会社 リニュー<br>あればロゴを入れる</div>
  <p class="license">古物商許可番号　大阪府公安委員会 第000000000号<br>一般廃棄物収集運搬業 許可番号 No.00000000</p>

  <p class="call-bar">まずはお電話でご相談ください!</p>
  <div class="tel">
    <svg width="38" height="38" viewBox="0 0 24 24"><path fill="var(--orange)" d="M6.6 10.8c1.4 2.8 3.8 5.1 6.6 6.6l2.2-2.2c.3-.3.7-.4 1-.2 1.1.4 2.3.6 3.6.6.6 0 1 .4 1 1V20c0 .6-.4 1-1 1C10.6 21 3 13.4 3 4c0-.6.4-1 1-1h3.5c.6 0 1 .4 1 1 0 1.3.2 2.5.6 3.6.1.3 0 .7-.2 1z"/></svg>
    <span class="label">TEL</span><span class="num">06-0000-0000</span>
  </div>
  <p class="info"><b>[営業時間]</b> 8:00～21:00 <b>[年中無休]</b><br>〒530-0000 大阪府大阪市北区見本町1-2-3 1F<br>詳しくはWEBもご覧ください。 www.ihinseiri-renew.jp</p>

  <div class="footer"></div>
</main>
</body>
</html>
```